Need a business card design. I am a Self Empowerment Life Coach.

A Life Coach is - a professional relationship designed to enhance an individual's ability to focus, make effective changes, develop oneself, achieve desired goals and maximize success in life. Coaching is about getting the very best out of someone and enabling them to make decisions that will improve their life. It is a unique way to help people look at where they are now and where they would like to be, and helps bridge the gap.

Tidal Grove Coaching is motivational, inspiring, positive, exciting and action driven. By raising awareness and encouraging others to take responsibility for their life, coaching can help people rise to their challenge and go further than you ever thought possible.

Industry/Entity Type

Business

Font styles to use
Other font styles liked:
• Bookman Old Style

Requirements
Must have
• Marlena Voskuil, ELI-MP
• Self Empowerment Coach
• 358.617.2083
• mv@thebrightpathguide.net
• The attached logo
Nice to have
• I would like to see some designs portrait and some landscape

```html
<!DOCTYPE html>
<html lang="en">
<head>
<meta charset="utf-8">
<title>Tidal Grove Coaching – Business Card</title>
<link rel="stylesheet" href="https://fonts.googleapis.com/css2?family=Libre+Baskerville:wght@400;700&display=swap">
<style>
  :root {
    --backdrop: #d9dadb;
    --card: #ffffff;
    --brand-navy: #1f3f8c;
    --brand-blue: #0a87c9;
    --panel-shadow: #1c2f7a;
    --sun: #f6c915;
    --ink-light: #ffffff;
  }
  * { box-sizing: border-box; margin: 0; padding: 0; }
  html, body { width: 1200px; height: 1200px; overflow: hidden; }
  body {
    background: var(--backdrop);
    display: flex; align-items: center; justify-content: center;
  }
  .business-card {
    position: relative;
    width: 1000px; height: 572px;
    background: var(--card);
    box-shadow: 0 6px 18px rgba(0,0,0,0.15);
  }
  .brand {
    position: absolute; left: 40px; top: 130px; width: 350px;
    display: flex; align-items: center; gap: 18px;
  }
  .brand-mark {
    width: 54px; height: 54px; border-radius: 50%;
    background: var(--sun); flex: none;
  }
  .brand-name {
    font-family: "Libre Baskerville", serif;
    font-weight: 700; color: var(--brand-navy);
    font-size: 40px; line-height: 1.15;
  }
  .contact-panel {
    position: absolute; left: 420px; top: 86px;
    width: 540px; height: 268px;
    background: var(--brand-blue);
    box-shadow: -10px 10px 0 var(--panel-shadow);
    color: var(--ink-light);
    font-family: "Libre Baskerville", serif;
    padding: 32px 24px 0 34px;
  }
  .holder-name { font-size: 33px; font-weight: 700; }
  .holder-credential { font-size: 22px; font-weight: 400; }
  .holder-role { font-size: 23px; margin-top: 6px; margin-bottom: 20px; }
  .contact-line { display: flex; align-items: center; gap: 12px; font-size: 24px; margin-top: 8px; }
  .contact-icon { width: 20px; height: 20px; flex: none; }
</style>
</head>
<body>
  <div class="business-card">
    <div class="brand">
      <div class="brand-mark"></div>
      <div class="brand-name">Tidal Grove<br>Coaching</div>
    </div>
    <div class="contact-panel">
      <div><span class="holder-name">Marlena Voskuil</span><span class="holder-credential">, ELI-MP</span></div>
      <div class="holder-role">Self Empowerment Coach</div>
      <div class="contact-line">
        <svg class="contact-icon" viewBox="0 0 20 20" aria-hidden="true">
          <circle cx="10" cy="10" r="10" fill="#0b5e96"/>
          <path d="M6 5.5l2 -.5 1.2 2.6-1.2 1a6 6 0 0 0 3 3l1-1.2 2.6 1.2-.5 2c-4.5.3-8.4-3.6-8.1-8.1z" fill="#fff"/>
        </svg>
        <span>358-617-2083</span>
      </div>
      <div class="contact-line">
        <svg class="contact-icon" viewBox="0 0 20 20" aria-hidden="true">
          <circle cx="10" cy="10" r="10" fill="#0b5e96"/>
          <rect x="5" y="6.5" width="10" height="7" fill="#fff"/>
          <path d="M5 6.5l5 4 5-4" fill="none" stroke="#0b5e96" stroke-width="1.2"/>
        </svg>
        <span>mv@thebrightpathguide.net</span>
      </div>
    </div>
  </div>
</body>
</html>
```